business card for a drum shop (musical intsruments)
north ridge beats
Use same font as used in my logo
marcus hollen
4127 Garvey Oakes Ct
Lower Fenwick, Md 20691
marcus.hollen517@quellmail.net
northridgebeats.com
yes, drum image in middle with url at botton
we will upload ai file shortly. please use this for now.

```html
<!DOCTYPE html>
<html lang="en">
<head>
<meta charset="utf-8">
<title>North Ridge Beats – Business Card</title>
<link href="https://fonts.googleapis.com/css2?family=Montserrat:wght@300;400&display=swap" rel="stylesheet">
<style>
  :root {
    --backdrop: #8c8c8c;
    --ink: #1c1716;
    --paper: #ffffff;
    --soft: #e9e9e9;
  }
  * { margin: 0; padding: 0; box-sizing: border-box; }
  html, body {
    width: 1200px; height: 908px; overflow: hidden;
    background: var(--backdrop);
    font-family: "Montserrat", sans-serif;
  }
  .stage {
    width: 1200px; height: 908px;
    display: flex; align-items: center; justify-content: center; gap: 40px;
  }
  .card {
    position: relative;
    width: 550px; height: 314px;
    border-radius: 16px;
    overflow: hidden;
    box-shadow: 0 6px 18px rgba(0,0,0,.3);
  }

  /* Back side */
  .card-back {
    background: var(--ink);
    color: var(--paper);
    text-align: center;
  }
  .back-mark {
    position: absolute; top: 50px; left: 0; right: 0;
    display: flex; flex-direction: column; align-items: center; gap: 12px;
  }
  .back-mark .mark-circle {
    width: 78px; height: 78px; border-radius: 50%;
    border: 3px solid var(--paper);
  }
  .back-mark .brand {
    font-weight: 300; font-size: 15px; letter-spacing: 5px; text-transform: uppercase;
  }
  .back-copy {
    position: absolute; left: 0; right: 0; top: 196px;
    font-weight: 300; font-size: 12.5px; line-height: 18px;
  }
  .back-url { margin-top: 6px; }

  /* Front side */
  .card-front { background: var(--paper); color: var(--ink); }
  .front-art { position: absolute; inset: 0; }
  .services {
    position: absolute; right: 34px; top: 40px;
    list-style: none; text-align: right;
    color: var(--paper); font-weight: 300; font-size: 14px; line-height: 20px;
  }
  .services li::after {
    content: ""; display: inline-block; width: 5px; height: 5px; border-radius: 50%;
    background: var(--paper); margin-left: 7px; vertical-align: middle;
  }
  .front-logo {
    position: absolute; left: 30px; top: 148px;
    display: flex; align-items: center; gap: 12px;
  }
  .front-logo .mark-circle {
    width: 38px; height: 38px; border-radius: 50%; background: var(--ink);
  }
  .front-logo .brand {
    font-weight: 300; font-size: 17px; letter-spacing: 5px; text-transform: uppercase;
  }
  .person {
    position: absolute; left: 30px; top: 200px;
    font-weight: 400; font-size: 22px;
  }
  .contact {
    position: absolute; left: 30px; top: 236px;
    list-style: none; font-weight: 300; font-size: 11.5px; line-height: 15px;
  }
  .contact li { display: flex; align-items: center; gap: 6px; }
  .contact svg { width: 11px; height: 11px; flex: none; }
</style>
</head>
<body>
<main class="stage">

  <section class="card card-back" aria-label="Card back">
    <div class="back-mark">
      <span class="mark-circle"></span>
      <span class="brand">north ridge beats</span>
    </div>
    <div class="back-copy">
      <p>We buy, sell, rent, repair and teach all things drums.</p>
      <p>Music lessons for drums, bass, guitar and piano.</p>
      <p>Full band rehearsal and drum practice studios.</p>
      <p class="back-url">www.northridgebeats.com</p>
    </div>
  </section>

  <section class="card card-front" aria-label="Card front">
    <svg class="front-art" viewBox="0 0 550 314" aria-hidden="true">
      <path d="M0 0 H550 V240 C470 150 330 118 180 128 C110 132 50 140 0 150 Z" fill="var(--ink)"/>
      <path d="M40 140 C160 122 360 118 520 226" fill="none" stroke="var(--ink)" stroke-width="2"/>
      <circle cx="40" cy="140" r="9" fill="var(--ink)"/>
      <circle cx="520" cy="226" r="6" fill="var(--ink)"/>
    </svg>

    <ul class="services">
      <li>drums</li>
      <li>music lessons</li>
      <li>rehearsal space</li>
    </ul>

    <div class="front-logo">
      <span class="mark-circle"></span>
      <span class="brand">north ridge beats</span>
    </div>

    <h1 class="person">Marcus Hollen</h1>

    <ul class="contact">
      <li>4127 Garvey Oakes Ct</li>
      <li>Lower Fenwick, Md 20691</li>
      <li>
        <svg viewBox="0 0 12 12"><circle cx="6" cy="6" r="6" fill="var(--ink)"/><path d="M4 3.2 L5 5 L4.4 5.6 Q5.4 7.4 6.6 7.8 L7.2 7.1 L8.8 8 L8.2 9 Q5 9 3.2 4 Z" fill="var(--paper)"/></svg>
        301-555-0142
      </li>
      <li>
        <svg viewBox="0 0 12 12"><circle cx="6" cy="6" r="6" fill="var(--ink)"/><rect x="3" y="4" width="6" height="4.2" fill="none" stroke="var(--paper)" stroke-width=".9"/><path d="M3 4 L6 6.4 L9 4" fill="none" stroke="var(--paper)" stroke-width=".9"/></svg>
        marcus.hollen517@quellmail.net
      </li>
      <li>
        <svg viewBox="0 0 12 12"><circle cx="6" cy="6" r="6" fill="var(--ink)"/><circle cx="6" cy="6" r="3.2" fill="none" stroke="var(--paper)" stroke-width=".9"/><path d="M2.8 6 H9.2 M6 2.8 V9.2" stroke="var(--paper)" stroke-width=".8"/></svg>
        www.northridgebeats.com
      </li>
    </ul>
  </section>

</main>
</body>
</html>
```